Grafitti Inspired Underwear Brand Needs Website

Rory's Briefs needs a website concept for our upcoming ecommerce site. Rory’s Briefs is an underwear line targeting a male demographic between 16 and 25. The logo is in the attachments. The brand is a colorful, rebellious underwear brand targeting men who are all about getting noticed and having a good time. And especially about meeting women. We need a website concept than will transport the audience into a world of rebellion, color and fun. We are totally open to ideas, but our initial thought is its an urban, graffiti jungle. It should be a transportive web environment that will make the audience feel they are entering this other world. It could be a street setting or it could be an alleyway (googling grafitti alleyway gives some ideas) or something else.

One challenge will be to create this colorful setting against which the various navigation tabs and product pictures will stand out in such a way as to allow easy e-commerce. Maybe the setting could be a building or garage with windows that the tabs would be set against for visibility.

Here is something we really like, but we have no idea how to make the various navigation tabs visible against a background as colorful and varied as this.

http://backdropvault.example/w/Xk7Tn2p

The brand is based on colorful and edgy designs that may certainly be provocative and even sexist in some minds. Similar brands are Pelotaverde and Lasse Vikstrand (before the went unisex fitness.) Please visit those brand sites to get an idea of what the product will look like.

From an executional perspective, the primary navigation tabs are in the attached map.

Again, this is an ecommerce site so saleable product must be easily visible on the homepage and elsewhere. The basic structure should be pretty standard with Hero A’s, Hero B’s, product shots and promotion boxes all very visible, but what we need is a really cool environment concept.

Primary navigation tabs should be horizontal across the top of the site in a pretty standard fashion and are:

1. Dangerous Rory’s
2. Wild Rory’s
3. Plain Rory’s
4. All the Damn Rory’s
5. Design Rory’s
6. Rory’s Life
7. Rory’s Jokes
8. About Rory’s

Target Market(s)

Men 16-25

Number of Pages Required

1 page

Requirements
Must have
• Brand Logo.
Nice to have
• Fun use of the devil/heart logo

```html
<!DOCTYPE html>
<html lang="en">
<head>
<meta charset="utf-8">
<title>Rory's Briefs</title>
<link rel="stylesheet" href="https://fonts.googleapis.com/css2?family=Oswald:wght@300;400;500;600&display=swap">
<style>
:root{
  --ink:#ffffff;
  --night:#1c1c1c;
  --bar:#262626;
  --coal:#2b2b2b;
  --foot:#121212;
  --yellow:#f5c518;
  --red:#e0443a;
  --green:#2ecc71;
  --teal:#3fd1b4;
  --purple:#7a3bd1;
  --muted:#cfcfcf;
}
*{margin:0;padding:0;box-sizing:border-box}
html,body{width:669px;height:1200px;overflow:hidden;background:var(--night)}
body{font-family:'Oswald',sans-serif;color:var(--ink);position:relative}
.page{position:relative;width:669px;height:1200px;overflow:hidden}
.abs{position:absolute}

/* navigation */
.nav{left:0;top:0;width:669px;height:40px;background:var(--bar);z-index:5}
.nav-item{position:absolute;top:9px;width:50px;text-align:center;font-size:6.5px;line-height:10px;letter-spacing:.3px;text-transform:uppercase;color:#e8e8e8}
.nav-item.is-active{color:var(--yellow);border-bottom:2px solid var(--yellow);height:31px}
.brand-tab{position:absolute;left:268px;top:0;width:134px;height:40px}
.brand-name{position:absolute;left:0;top:12px;width:134px;text-align:center;font-size:14px;font-weight:600;color:var(--purple);letter-spacing:.3px}
.brand-dot{display:inline-block;width:8px;height:8px;border-radius:50%;background:var(--green);margin-right:4px;vertical-align:1px}

/* hero */
.hero{left:0;top:40px;width:669px;height:234px;background:linear-gradient(90deg,#7a2d3a 0%,#3c4a7a 22%,#9a8f8a 50%,#3d6b6e 78%,#5a2f6a 100%)}
.hero-shade{left:0;top:40px;width:669px;height:234px;background:radial-gradient(ellipse at 50% 60%,rgba(0,0,0,0) 0%,rgba(0,0,0,.35) 80%)}
.hero-title{left:0;top:104px;width:669px;text-align:center;font-size:25px;font-weight:500;letter-spacing:3px}
.hero-sub{left:0;top:136px;width:669px;text-align:center;font-size:16px;font-weight:500;letter-spacing:3.2px}
.hero-cta{left:282px;top:188px;width:104px;height:24px;background:var(--yellow);color:#1a1a1a;font-size:15px;font-weight:600;text-align:center;line-height:24px;letter-spacing:.6px}
.scroll-cue{left:322px;top:262px;width:25px;height:25px;border-radius:50%;background:var(--coal);z-index:3}

/* promos */
.promos{left:0;top:274px;width:669px;height:168px;background:var(--coal)}
.promo{top:304px;width:298px;height:110px;overflow:hidden}
.promo-photo{position:absolute;inset:0}
.promo-title{position:absolute;left:8px;top:20px;font-size:20px;font-weight:600;letter-spacing:1px}
.promo-band{position:absolute;left:0;top:57px;width:100%;height:24px;line-height:24px;font-size:14px;font-weight:300;letter-spacing:1px;padding-left:8px}

/* arrivals */
.arrivals{left:0;top:442px;width:669px;height:314px;background:linear-gradient(180deg,#4a423d 0%,#3a3532 50%,#2c2a29 100%)}
.section-title{left:0;width:669px;text-align:center;font-weight:500;letter-spacing:1px}
.card{top:524px;width:129px;height:172px;background:rgba(120,120,120,.35)}
.card-line{position:absolute;left:0;top:0;width:100%;height:2px}
.card-photo{position:absolute;left:12px;top:36px;width:105px;height:88px;border-radius:4px}
.card-caption{position:absolute;left:0;bottom:0;width:100%;height:26px;background:rgba(30,30,30,.75);text-align:center;font-size:5.5px;line-height:8px;padding-top:5px;font-weight:500}
.card-caption s{color:var(--yellow);margin-right:6px}
.sale-tag{position:absolute;left:0;top:0;width:100%;height:14px;background:var(--yellow);color:var(--ink);font-size:6.5px;font-weight:600;text-align:center;line-height:14px}
.sizes{position:absolute;left:2px;top:6px;display:flex;gap:5px}
.size{width:14px;height:12px;border:1px solid #e8e8e8;font-size:5.5px;text-align:center;line-height:10px}
.size.is-off{opacity:.4}
.size.is-picked{border-color:var(--teal);color:var(--teal)}
.add-cart{position:absolute;left:44px;top:23px;font-size:5px;letter-spacing:.3px}
.slider-arrow{top:588px;width:14px;height:14px;border:1px solid #ddd;background:rgba(0,0,0,.4)}
.dots{left:320px;top:715px;display:flex;gap:5px}
.dot{width:6px;height:6px;border-radius:50%;background:#fff}
.dot.is-current{background:var(--green)}

/* about */
.intro{left:0;top:818px;width:669px;text-align:center;font-size:12px;line-height:24px;font-weight:300;letter-spacing:.3px}
.story{top:876px;width:193px;height:132px;overflow:hidden}
.story-photo{position:absolute;inset:0}
.story-title{position:absolute;left:0;top:9px;width:100%;text-align:center;font-size:17px;font-weight:500;letter-spacing:.5px}
.story-title span{border-bottom:1px solid #fff;padding-bottom:1px}
.story-text{position:absolute;left:7px;top:36px;width:180px;font-size:6.4px;line-height:15.5px;text-align:center;font-family:'Oswald',sans-serif;font-weight:300}
.story-btn{position:absolute;left:61px;top:100px;width:68px;height:16px;border:1.5px solid #fff;font-size:7.5px;font-weight:500;text-align:center;line-height:13px}
.story-btn.is-solid{background:#fff;color:#1a1a1a}

/* footer */
.footer{left:0;top:1050px;width:669px;height:150px;background:var(--foot)}
.foot-head{top:1066px;font-size:7.5px;font-weight:500;letter-spacing:.3px}
.foot-line{font-size:7px;font-weight:300;color:var(--muted);line-height:16px}
.contact-list{left:128px;top:1088px}
.contact-row{display:flex;align-items:flex-start;gap:7px}
.menu-list{left:294px;top:1089px;width:80px;text-align:center;text-transform:uppercase}
.news-note{left:447px;top:1092px;font-size:8px;font-weight:500}
.news-field{left:428px;top:1116px;width:112px;height:17px;background:#fff;color:#777;font-size:6.5px;font-weight:300;text-align:center;line-height:17px}
.news-btn{left:482px;top:1148px;width:58px;height:16px;background:var(--green);color:#111;font-size:7px;font-weight:600;text-align:center;line-height:16px}
.copyright{left:0;top:1190px;width:669px;text-align:center;font-size:5px;color:var(--muted)}
</style>
</head>
<body>
<div class="page">

  <!-- navigation -->
  <nav class="nav abs">
    <div class="nav-item" style="left:129px">Dangerous<br>Rory’s</div>
    <div class="nav-item is-active" style="left:178px">Plain<br>Rory’s</div>
    <div class="nav-item" style="left:228px">Design<br>Rory’s</div>
    <div class="brand-tab">
      <svg width="134" height="40" viewBox="0 0 134 40" class="abs" style="left:0;top:0">
        <path d="M0 0 Q14 0 20 18 Q27 38 50 38 L84 38 Q107 38 114 18 Q120 0 134 0 Z" fill="#f2f2f2"/>
      </svg>
      <div class="brand-name"><span class="brand-dot"></span>Rory’s Briefs</div>
    </div>
    <div class="nav-item" style="left:390px">About<br>Rory’s</div>
    <div class="nav-item" style="left:440px">Rory’s<br>Life</div>
    <div class="nav-item" style="left:489px">Rory’s<br>Jokes</div>
  </nav>

  <!-- hero -->
  <div class="hero abs" role="img" aria-label="Photo of a graffiti-covered alleyway"></div>
  <div class="hero-shade abs"></div>
  <h1 class="hero-title abs">RORY’S BRIEFS</h1>
  <p class="hero-sub abs">ARE YOU READY FOR REBELLION?</p>
  <div class="hero-cta abs">SHOP NOW</div>

  <!-- promos -->
  <section class="promos abs"></section>
  <div class="scroll-cue abs">
    <svg width="25" height="25" viewBox="0 0 25 25"><path d="M6 10 L12.5 16 L19 10" stroke="#fff" stroke-width="1.6" fill="none"/></svg>
  </div>
  <div class="promo abs" style="left:19px">
    <div class="promo-photo" role="img" aria-label="Photo of a tattooed couple" style="background:linear-gradient(90deg,#fbfbfb 0%,#f1eeec 45%,#cfc6c2 75%,#8c8480 100%)"></div>
    <div class="promo-title" style="color:var(--red)">FREE SHIPPING</div>
    <div class="promo-band" style="background:var(--red);width:298px">$45 TO QUALIFY , DOMESTIC ORDERS ONLY</div>
  </div>
  <div class="promo abs" style="left:352px">
    <div class="promo-photo" role="img" aria-label="Photo of a dancer in front of a graffiti shutter" style="background:linear-gradient(90deg,#6a3fa0 0%,#c23a7a 35%,#3a8ec2 65%,#7a2f8a 100%)"></div>
    <div class="promo-title" style="color:var(--yellow);left:92px">PROMOTIONS</div>
    <div class="promo-band" style="background:var(--yellow);text-align:center;padding-left:0">CHECK TODAY’S DEALS</div>
  </div>

  <!-- new arrivals -->
  <section class="arrivals abs" role="img" aria-label="Graffiti-painted brick wall backdrop"></section>
  <h2 class="section-title abs" style="top:474px;font-size:16px">NEW ARRIVALS</h2>

  <div class="slider-arrow abs" style="left:19px">
    <svg width="12" height="12" viewBox="0 0 12 12"><path d="M7.5 3 L4.5 6 L7.5 9" stroke="#fff" stroke-width="1.4" fill="none"/></svg>
  </div>
  <div class="slider-arrow abs" style="left:636px">
    <svg width="12" height="12" viewBox="0 0 12 12"><path d="M4.5 3 L7.5 6 L4.5 9" stroke="#fff" stroke-width="1.4" fill="none"/></svg>
  </div>

  <article class="card abs" style="left:50px">
    <div class="card-line" style="background:var(--teal)"></div>
    <div class="sizes">
      <div class="size is-off">XS</div><div class="size">S</div><div class="size">M</div><div class="size">L</div><div class="size is-picked">XL</div><div class="size">XXL</div>
    </div>
    <div class="add-cart">ADD TO CART</div>
    <div class="card-photo" role="img" aria-label="Product shot of maroon shorts with dancer print" style="background:linear-gradient(135deg,#6e1a2e,#c8452e,#e8902e)"></div>
    <div class="card-caption">MEN 1-PACK SHORTS “DANCERS”<br>32,95 USD</div>
  </article>
  <article class="card abs" style="left:198px">
    <div class="card-line" style="background:var(--red)"></div>
    <div class="card-photo" role="img" aria-label="Product shot of purple shorts with octopus print" style="background:linear-gradient(135deg,#d0354a,#6a3fb0,#3aa0b8)"></div>
    <div class="card-caption">MEN 1-PACK SHORTS “OCTORORY”<br>32,95 USD</div>
  </article>
  <article class="card abs" style="left:343px">
    <div class="sale-tag">ON SALE</div>
    <div class="card-photo" role="img" aria-label="Product shot of plain black shorts with lime waistband" style="background:linear-gradient(180deg,#b8e62e 0%,#b8e62e 10%,#1c1c1c 12%,#2e2e2e 100%)"></div>
    <div class="card-caption">MEN 1-PACK SHORTS “PLAIN”<br><s>32,95 USD</s>26,95 USD</div>
  </article>
  <article class="card abs" style="left:490px">
    <div class="card-line" style="background:var(--purple)"></div>
    <div class="card-photo" role="img" aria-label="Product shot of blue shorts with yellow pattern" style="background:linear-gradient(135deg,#2a6ad8,#3fa0e8,#e8c82e)"></div>
    <div class="card-caption">MEN 1-PACK SHORTS “WOMEN”<br>32,95 USD</div>
  </article>

  <div class="dots abs"><div class="dot is-current"></div><div class="dot"></div><div class="dot"></div></div>

  <!-- who are we -->
  <h2 class="section-title abs" style="top:779px;font-size:19px">WHO ARE WE?</h2>
  <p class="intro abs">The new underwear brand designing colorful, fun and rebellious<br>shorts for young men using high quality materials.</p>

  <article class="story abs" style="left:19px">
    <div class="story-photo" role="img" aria-label="Photo of a couple in red tones" style="background:linear-gradient(135deg,#4a2a30,#7a3a42,#3a2226)"></div>
    <h3 class="story-title"><span>ABOUT RORY’S</span></h3>
    <p class="story-text">Lorem ipsum dolor sit amet, consectetur adipiscing elit, sed do eiusmod tempor incididunt ut labore et dolore magna aliqua. Ut enim ad minim veniam, quis nostrud exercitation ullamco laboris nisi ut aliquip ex ea commodo consequat.</p>
    <div class="story-btn">LEARN MORE</div>
  </article>
  <article class="story abs" style="left:238px">
    <div class="story-photo" role="img" aria-label="Photo of a person in soft lilac light" style="background:linear-gradient(135deg,#8a8aa8,#c8c8dc,#5a5a78)"></div>
    <h3 class="story-title"><span>RORY’S LIFE</span></h3>
    <p class="story-text">Lorem ipsum dolor sit amet, consectetur adipiscing elit, sed do eiusmod tempor incididunt ut labore et dolore magna aliqua. Ut enim ad minim veniam, quis nostrud exercitation ullamco laboris nisi ut aliquip ex ea commodo consequat.</p>
    <div class="story-btn is-solid">LEARN MORE</div>
  </article>
  <article class="story abs" style="left:457px">
    <div class="story-photo" role="img" aria-label="Photo of dancers silhouetted against pink neon" style="background:linear-gradient(135deg,#3a1050,#c82a9a,#6a1a80)"></div>
    <h3 class="story-title"><span>RORY’S JOKES</span></h3>
    <p class="story-text">Lorem ipsum dolor sit amet, consectetur adipiscing elit, sed do eiusmod tempor incididunt ut labore et dolore magna aliqua. Ut enim ad minim veniam, quis nostrud exercitation ullamco laboris nisi ut aliquip ex ea commodo consequat.</p>
    <div class="story-btn">LEARN MORE</div>
  </article>

  <!-- footer -->
  <footer class="footer abs"></footer>
  <div class="foot-head abs" style="left:128px">CONTACT US</div>
  <div class="foot-head abs" style="left:315px">MAIN MENU</div>
  <div class="foot-head abs" style="left:497px">NEWSLETTER</div>

  <div class="contact-list abs">
    <div class="contact-row">
      <svg width="10" height="14" viewBox="0 0 10 14"><path d="M5 0 C2 0 0 2.2 0 5 C0 8.5 5 14 5 14 C5 14 10 8.5 10 5 C10 2.2 8 0 5 0 Z" fill="var(--green)"/><circle cx="5" cy="5" r="2" fill="var(--foot)"/></svg>
      <div class="foot-line">41 Mural Lane<br>Brickton, ST 00412</div>
    </div>
    <div class="contact-row">
      <svg width="10" height="10" viewBox="0 0 10 10" style="margin-top:3px"><path d="M2 0 L4 2.5 L3 4 Q4.5 6 6 7 L7.5 6 L10 8 L8.5 10 Q4 9.5 0 2 Z" fill="var(--green)"/></svg>
      <div class="foot-line">0 00-555-010-199</div>
    </div>
    <div class="contact-row">
      <svg width="10" height="8" viewBox="0 0 10 8" style="margin-top:4px"><rect width="10" height="8" fill="var(--green)"/><path d="M0 0 L5 4.5 L10 0" stroke="var(--foot)" stroke-width="1" fill="none"/></svg>
      <div class="foot-line">youremailadress@example.com</div>
    </div>
  </div>

  <div class="menu-list abs foot-line">
    Dangerous Rory’s<br>Plain Rory’s<br>Design Rory’s<br>Rory’s Life<br>Rory’s Jokes
  </div>

  <div class="news-note abs">Lorem ipsum dolor sit amet</div>
  <div class="news-field abs">enter your e-mail here</div>
  <div class="news-btn abs">SUBSCRIBE</div>

  <div class="copyright abs">COPYRIGHT 2016 RORY’S BRIEFS</div>
</div>
</body>
</html>
```